We need a website for an ice cream shop "otter ice cream"

We are opening an ice cream shop called "otter ice cream". We already have a logo (photo attached). The ice cream shop will be in the style of "Coral Motel" movie - palm trees, sunset, there will be a flamingo on the wall, so basically sunset, beach, Miami style. We would like the website to be colorful, colors of sunset, colorful buildings, girls wearing vintage roller skates. You can get inspiration from the "Coral Motel" movie. We would like the website to be playful, a little vintage, not boring. The website should attract people's attention.

Target Market(s)

everyone

Industry/Entity Type

ice cream shop

Number of Pages Required

5+ page

Font styles to use
Sans Serif
Script

Colors
0094D4
00A9DD
6FCCEA
C7EBF8
E9F6FB
FFC000
F8CF3A
FAE287
FDF2CF
FEFAEE
F0912C
F2A743
F7CA91
FBE8D2
FDF5EE
EE7325
F08F49
F5BC92
FAE3D3
FDF4ED
E54698
E96AAD
F1A4CE
F9D9EA
FCEFF6
A7469A
B969AE
D3A5CF
EDDBEB
F8F0F9

Requirements
Must have
• tropical, Miami style, sunset
Nice to have
• palm trees, flamingo, girls on vintage roller skates, sea, colorful buildings

```html
<!DOCTYPE html>
<html lang="en">
<head>
<meta charset="utf-8">
<title>About Us · otter ice cream</title>
<link rel="stylesheet" href="https://fonts.googleapis.com/css2?family=Bebas+Neue&family=Lobster&family=Caladea:wght@700&family=Exo+2:wght@600;700&display=swap">
<style>
  :root {
    --orange: #EE7325;
    --orange-deep: #E0601A;
    --white: #FFFFFF;
    --ink: #111111;
    --navy: #1D3E7A;
    --search: #ECEAEA;
    --search-text: #C9C6C6;
    --sky-top: #8A80A8;
    --sky-mid: #C3A9CC;
    --sky-pink: #E9B9C6;
    --sky-peach: #FBA58A;
    --sky-gold: #FFD58C;
    --title-box: rgba(190, 140, 190, 0.6);
  }
  * { box-sizing: border-box; margin: 0; padding: 0; }
  html, body { width: 1200px; height: 1173px; overflow: hidden; background: var(--white); }
  .page { position: relative; width: 1200px; height: 1173px; }

  .site-header {
    position: absolute; left: 0; top: 0; width: 1200px; height: 107px;
    background: var(--orange);
  }
  .brand {
    position: absolute; left: 82px; top: 34px; display: flex; align-items: center; gap: 8px;
    font-family: "Bebas Neue", sans-serif; font-size: 26px; color: var(--white);
    letter-spacing: 0.5px; line-height: 1;
  }
  .brand-dot { width: 40px; height: 40px; border-radius: 50%; background: var(--navy); flex: none; }
  .main-nav {
    font-family: "Bebas Neue", sans-serif; font-size: 30px; color: var(--white); line-height: 29px;
  }
  .main-nav a {
    position: absolute; top: 44px; height: 29px; color: inherit; text-decoration: none;
    white-space: nowrap; padding-top: 1px;
  }
  .main-nav .nav-menu { left: 500px; }
  .main-nav .nav-photo { left: 597px; }
  .main-nav .nav-contact { left: 690px; }
  .main-nav .nav-about {
    left: 778px; width: 99px; text-align: center;
    background: var(--orange-deep); border-radius: 14px;
  }
  .search {
    position: absolute; left: 923px; top: 41px; width: 234px; height: 40px;
    background: var(--search); border-radius: 20px;
    display: flex; align-items: center; padding-left: 12px; gap: 28px;
    font-family: "Exo 2", sans-serif; font-weight: 600; font-size: 14px; color: var(--search-text);
  }

  .hero {
    position: absolute; left: 0; top: 107px; width: 1200px; height: 889px;
    background: linear-gradient(180deg, var(--sky-top) 0%, var(--sky-mid) 50%, var(--sky-pink) 72%, var(--sky-peach) 90%, var(--sky-gold) 100%);
  }
  .title-box {
    position: absolute; left: 289px; top: 172px; width: 622px; height: 154px;
    background: var(--title-box); border-radius: 20px;
    box-shadow: 0 3px 5px rgba(80, 50, 90, 0.35);
    display: flex; align-items: center; justify-content: center;
  }
  .title-box h1 {
    font-family: "Lobster", cursive; font-weight: 400; font-size: 150px; color: var(--white);
    line-height: 1; margin-top: -12px; white-space: nowrap;
  }
  .story {
    position: absolute; left: 98px; top: 398px; width: 1004px; text-align: center;
    font-family: "Caladea", serif; font-weight: 700; font-size: 30px; line-height: 34px; color: var(--ink);
  }
  .hero-mark {
    position: absolute; left: 0; top: 697px; width: 1200px;
    display: flex; flex-direction: column; align-items: center; gap: 6px;
    font-family: "Bebas Neue", sans-serif; font-size: 26px; color: var(--white);
    letter-spacing: 0.5px; line-height: 1;
  }
  .hero-mark .brand-dot { width: 100px; height: 100px; }

  .site-footer {
    position: absolute; left: 0; top: 996px; width: 1200px; height: 177px;
    background: var(--orange); border: 3px solid var(--white); border-bottom: 0;
    font-family: "Exo 2", sans-serif; color: var(--white);
  }
  .footer-col { position: absolute; top: 29px; }
  .footer-col h2 { font-weight: 700; font-size: 25px; line-height: 30px; margin-bottom: 2px; }
  .footer-col p { font-weight: 600; font-size: 15px; line-height: 25px; }
  .col-address { left: 267px; top: 31px; }
  .col-address h2 { font-size: 27px; }
  .col-contact { left: 546px; }
  .col-hours { left: 849px; }
  .copyright {
    position: absolute; left: 0; right: 0; top: 134px; text-align: center;
    font-weight: 600; font-size: 12px;
  }
</style>
</head>
<body>
<div class="page">
  <header class="site-header">
    <div class="brand"><span class="brand-dot"></span>otter ice cream</div>
    <nav class="main-nav">
      <a class="nav-menu" href="#">MENU</a>
      <a class="nav-photo" href="#">PHOTO</a>
      <a class="nav-contact" href="#">CONTACT</a>
      <a class="nav-about" href="#">ABOUT US</a>
    </nav>
    <div class="search">
      <svg width="36" height="26" viewBox="0 0 36 26" aria-hidden="true">
        <circle cx="22" cy="10" r="8" fill="none" stroke="#B9B6B6" stroke-width="2"/>
        <line x1="16" y1="16" x2="4" y2="24" stroke="#B9B6B6" stroke-width="3" stroke-linecap="round"/>
      </svg>
      <span>Search...</span>
    </div>
  </header>

  <main class="hero" role="img" aria-label="Soft pastel sunset sky with pink and violet clouds fading into golden light">
    <div class="title-box"><h1>About Us</h1></div>
    <p class="story">"Lorem ipsum dolor sit amet, consectetur adipiscing elit, sed do eiusmod tempor incididunt ut labore et dolore magna aliqua. Ut enim ad minim veniam, quis nostrud exercitation ullamco laboris nisi ut aliquip ex ea commodo consequat. Duis aute irure dolor in reprehenderit in voluptate velit esse cillum dolore eu fugiat nulla pariatur. Excepteur sint occaecat cupidatat non proident, sunt in culpa qui officia deserunt mollit anim id est laborum."</p>
    <div class="hero-mark"><span class="brand-dot"></span>otter ice cream</div>
  </main>

  <footer class="site-footer">
    <div class="footer-col col-address">
      <h2>ADDRESS</h2>
      <p>Lorem Ipsum dolor</p>
      <p>Lorem Ipsum dolor</p>
    </div>
    <div class="footer-col col-contact">
      <h2>CONTACT</h2>
      <p>hello@otterscoops.com</p>
      <p>Tel : 0555-0142</p>
    </div>
    <div class="footer-col col-hours">
      <h2>HOURS</h2>
      <p>OPEN DAILY</p>
      <p>7 AM - 6 PM</p>
    </div>
    <p class="copyright">©2022 by myself. Proudly created with Sketchloft</p>
  </footer>
</div>
</body>
</html>
```